Social Media Cover and Profile

We already have our own logo. We just need a fresh design on our social media pages. We are not happy with our current designs. We would like to incorporate our WHEE billboard and the colors are blue (#05143f) and white. You can also incorporate silver as well. We are a family law office (Divorce and Custody) We no longer want to incorporate the Beacon of Dunmore photo that we are currently using. You can look at our Facebook page; The Law Office of Miles T. Brandow.

Target Market(s)

Potential Clients

Industry/Entity Type

Family Law

Logo Text

Our Logo Is The Law Office of Miles T. Brandow with the Sheild

Requirements
Must have
• Text to include:
Central Pennslyvania's Premier Family Law Firm

Ability to be resized to and used as all images in social media, including but not limited to: Youtube Channel art, Facebook Cover and Profile.
Nice to have
• Darker color but we are open to "bright" ideas.

```html
<!DOCTYPE html>
<html lang="en">
<head>
<meta charset="utf-8">
<title>Miles T. Brandow – Social Cover and Profile</title>
<link href="https://fonts.googleapis.com/css2?family=Cinzel:wght@500;600&display=swap" rel="stylesheet">
<style>
  :root {
    --navy: #05143f;
    --navy-deep: #030c2c;
    --silver: #c9ced8;
    --white: #ffffff;
    --stage: #e8ebf1;
  }
  html, body {
    margin: 0;
    width: 1151px;
    height: 1200px;
    overflow: hidden;
    background: var(--stage);
  }
  .canvas {
    position: relative;
    width: 1151px;
    height: 1200px;
  }
  .cover {
    position: absolute;
    left: 40px;
    top: 70px;
    width: 1071px;
    height: 407px;
    display: block;
  }
  .cover-kicker {
    font-family: "Cinzel", serif;
    font-weight: 500;
    font-size: 16px;
    fill: var(--white);
    letter-spacing: 0.3px;
  }
  .cover-title {
    font-family: "Cinzel", serif;
    font-weight: 600;
    font-size: 35px;
    fill: var(--white);
    letter-spacing: 0.5px;
  }
  .billboard-name {
    font-family: "Cinzel", serif;
    font-weight: 600;
    font-size: 17px;
    fill: var(--navy);
  }
  .billboard-line {
    font-family: "Cinzel", serif;
    font-weight: 500;
    font-size: 4px;
    fill: var(--navy);
  }
  .profile {
    position: absolute;
    left: 425px;
    top: 590px;
    width: 300px;
    height: 300px;
    border-radius: 50%;
    background: var(--white);
    border: 6px solid var(--navy);
    box-sizing: border-box;
    display: flex;
    align-items: center;
    justify-content: center;
    text-align: center;
  }
  .profile-name {
    font-family: "Cinzel", serif;
    font-weight: 600;
    font-size: 24px;
    line-height: 1.25;
    color: var(--navy);
    margin: 0 34px;
  }
</style>
</head>
<body>
<main class="canvas">
  <svg class="cover" viewBox="0 0 820 312" xmlns="http://www.w3.org/2000/svg">
    <defs>
      <linearGradient id="photoTone" x1="0" y1="0" x2="1" y2="1">
        <stop offset="0" stop-color="#e9e6e2"/>
        <stop offset="0.5" stop-color="#d8c4b4"/>
        <stop offset="1" stop-color="#7c8aa6"/>
      </linearGradient>
      <linearGradient id="decorTone" x1="0" y1="0" x2="1" y2="0">
        <stop offset="0" stop-color="#0d2057" stop-opacity="0.7"/>
        <stop offset="1" stop-color="#05143f" stop-opacity="0"/>
      </linearGradient>
      <radialGradient id="justiceTone" cx="0.5" cy="0.5" r="0.5">
        <stop offset="0" stop-color="#a9b2c8" stop-opacity="0.45"/>
        <stop offset="0.6" stop-color="#4a5b88" stop-opacity="0.25"/>
        <stop offset="1" stop-color="#05143f" stop-opacity="0"/>
      </radialGradient>
    </defs>
    <rect class="cover-bg" width="820" height="312" fill="var(--navy)"/>
    <rect class="cover-decor" x="0" y="0" width="400" height="312" fill="url(#decorTone)" role="img" aria-label="Faint scales of justice and statue motif in the background"/>

    <text class="cover-kicker" x="66" y="108">Central Pennslyvania's Premier</text>
    <text class="cover-title" x="66" y="145">Family Law Firm</text>

    <path class="photo-frame" d="M408,49 H583 V150 C583,205 545,245 495,268 C445,245 408,205 408,150 Z" fill="var(--navy-deep)" stroke="var(--silver)" stroke-width="2"/>
    <path class="photo-fill" d="M414,56 H577 V150 C577,200 542,236 495,260 C448,236 414,200 414,150 Z" fill="url(#photoTone)" role="img" aria-label="Photo of a mother and daughter embracing with a bouquet of tulips"/>

    <ellipse class="justice-art" cx="686" cy="150" rx="86" ry="66" fill="url(#justiceTone)" role="img" aria-label="White line illustration of Lady Justice holding scales"/>

    <rect class="billboard" x="686" y="196" width="104" height="31" fill="var(--white)"/>
    <text class="billboard-name" x="738" y="216" text-anchor="middle">WHEE</text>
    <text class="billboard-line" x="738" y="223.5" text-anchor="middle">Miles T. Brandow · Family Law</text>
  </svg>

  <div class="profile">
    <p class="profile-name">The Law Office of Miles T. Brandow</p>
  </div>
</main>
</body>
</html>
```